Business card for Sports Apparel business

DOUBLE SIDED DESIGN
We need business cards for a new sports apparel business. We are developing a protective headband for soccer initially.
Corvell is focused on designing and developing head protection products to reduce the likelihood of concussion when playing sports. Exploring and understanding medical insights, material science research, current and former players experiences and governing bodies guidelines has allowed Corvell to develop the safety, style, form and function requirements of a suitable product to bring to market.
Target Market(s)
Mums buying kits for the sons and daughters. Amateur footballers.
Industry/Entity Type
Sporting Good
Contact Information for Business Card
Martin Ashgrove - CEO
Mobile: +44 7391608254
Email: martin@corvell.co.uk
Tel: 0208 5143927
Helena Pardoe - COO
Mob: +44 7356 409183
Email: helena@corvell.co.uk
Tel: 0208 5143927
Duncan Wyvern - CCO
Mob: +44 7468 230517
Email: duncan@corvell.co.uk
Tel: 0208 5143927
Look and feel

```html
<!DOCTYPE html>
<html lang="en">
<head>
<meta charset="utf-8">
<title>Corvell Business Card</title>
<link rel="stylesheet" href="https://fonts.googleapis.com/css2?family=Montserrat:wght@400;500;600;700&display=swap">
<style>
  :root {
    --brand-blue: #0b5c9c;
    --brand-blue-deep: #08497f;
    --ink: #222428;
    --ink-soft: #3a3d42;
    --card-white: #ffffff;
    --backdrop: #e6e8eb;
  }
  * { margin: 0; padding: 0; box-sizing: border-box; }
  html, body { width: 1200px; height: 900px; overflow: hidden; }
  body {
    background: var(--backdrop);
    font-family: "Montserrat", sans-serif;
    display: flex;
    flex-direction: column;
    align-items: center;
    justify-content: center;
    gap: 40px;
  }
  .card {
    position: relative;
    width: 680px;
    height: 390px;
    background: var(--card-white);
    border-radius: 26px;
    overflow: hidden;
    box-shadow: 0 6px 18px rgba(0,0,0,0.12);
  }
  .card-waves { position: absolute; inset: 0; width: 100%; height: 100%; }
  .wave-fill { fill: var(--brand-blue); }
  .wave-accent { fill: var(--brand-blue-deep); }

  .wordmark {
    position: absolute;
    display: flex;
    align-items: center;
    gap: 14px;
    color: var(--brand-blue);
    font-weight: 700;
    text-transform: uppercase;
    letter-spacing: 0.04em;
  }
  .wordmark-square { background: var(--brand-blue); flex: none; }

  .card-front .wordmark { left: 50%; top: 148px; transform: translateX(-50%); font-size: 52px; }
  .card-front .wordmark-square { width: 26px; height: 26px; }

  .card-back .wordmark { left: 70px; top: 48px; font-size: 34px; }
  .card-back .wordmark-square { width: 18px; height: 18px; }

  .contact-list {
    position: absolute;
    left: 70px;
    top: 140px;
    list-style: none;
    display: flex;
    flex-direction: column;
    gap: 14px;
    font-size: 16px;
    color: var(--ink-soft);
  }
  .contact-item { display: flex; align-items: center; gap: 14px; }
  .contact-icon { width: 18px; height: 18px; flex: none; stroke: var(--brand-blue); fill: none; stroke-width: 1.6; stroke-linecap: round; stroke-linejoin: round; }

  .person {
    position: absolute;
    right: 56px;
    top: 170px;
    text-align: right;
  }
  .person-name {
    color: var(--brand-blue);
    font-size: 22px;
    font-weight: 600;
    text-transform: uppercase;
    letter-spacing: 0.03em;
  }
  .person-rule { height: 1.5px; background: var(--ink); width: 240px; margin: 8px 0 6px auto; }
  .person-role {
    color: var(--ink);
    font-size: 20px;
    font-weight: 600;
    letter-spacing: 0.05em;
  }
</style>
</head>
<body>

  <section class="card card-front" aria-label="Card front">
    <svg class="card-waves" viewBox="0 0 680 390" preserveAspectRatio="none" aria-hidden="true">
      <path class="wave-fill" d="M250,0 C400,30 560,110 680,210 L680,0 Z"/>
      <path class="wave-fill" d="M0,150 C60,300 240,300 420,300 C540,300 630,340 680,390 L0,390 Z"/>
      <path class="wave-accent" d="M0,70 C20,170 90,250 260,290 C120,240 40,170 0,70 Z"/>
    </svg>
    <div class="wordmark">
      <span class="wordmark-square"></span>
      <span class="wordmark-name">Corvell</span>
    </div>
  </section>

  <section class="card card-back" aria-label="Card back">
    <svg class="card-waves" viewBox="0 0 680 390" preserveAspectRatio="none" aria-hidden="true">
      <path class="wave-fill" d="M0,0 L60,0 C30,60 12,130 0,210 Z"/>
      <path class="wave-fill" d="M430,0 C540,20 620,50 680,90 L680,0 Z"/>
      <path class="wave-fill" d="M200,390 C300,330 460,320 560,300 C620,290 660,270 680,240 L680,390 Z"/>
      <path class="wave-accent" d="M300,285 C420,270 540,280 640,330 C540,300 420,290 300,285 Z"/>
    </svg>

    <div class="wordmark">
      <span class="wordmark-square"></span>
      <span class="wordmark-name">Corvell</span>
    </div>

    <ul class="contact-list">
      <li class="contact-item">
        <svg class="contact-icon" viewBox="0 0 24 24" aria-hidden="true"><path d="M5 3h4l2 5-3 2a12 12 0 0 0 6 6l2-3 5 2v4a2 2 0 0 1-2 2A18 18 0 0 1 3 5a2 2 0 0 1 2-2z"/></svg>
        <span>+44 7391608254</span>
      </li>
      <li class="contact-item">
        <svg class="contact-icon" viewBox="0 0 24 24" aria-hidden="true"><rect x="3" y="5" width="18" height="14" rx="1"/><path d="M3 6l9 7 9-7"/></svg>
        <span>martin@corvell.co.uk</span>
      </li>
      <li class="contact-item">
        <svg class="contact-icon" viewBox="0 0 24 24" aria-hidden="true"><rect x="4" y="9" width="16" height="11" rx="2"/><path d="M3 9c2-4 16-4 18 0"/><circle cx="12" cy="14.5" r="2.5"/></svg>
        <span>0208 5143927</span>
      </li>
    </ul>

    <div class="person">
      <p class="person-name">Martin Ashgrove</p>
      <div class="person-rule"></div>
      <p class="person-role">CEO</p>
    </div>
  </section>

</body>
</html>
```